Orthopaedic Clinic Needs facebook page

Orthopaedic Clinic needs facebook page. The name of our clinic is Larchmont Orthopaedics. We focus on hip and knee orthopaedic conditions, as well as general orthopaedics. The main services are total knee replacements, total hip replacements, sports injury of the knee, hip fractures. Unique selling points of our service would be 1. Patient Centred Care, 2. Value Driven, 3. 2 Double-Fellowship Trained Surgeons.

Colour scheme should fit the logo design and be within the general colour recommendations of a medical clinic.

The design should be modern, eye catching, draws the end user to the website.

We would like to design our facebook page for future social media marketing.
In accordance with local advertisement regulations pertaining to medical clinics, no statements must have any information or laudatory statements such as the use of best, better, breakthrough, champions, or any statements that imply superiority and that may create unjustified expectations of services.

Target Market(s)

Patients
Friends family and relatives of patients.

Font styles to use
Serif
Sans Serif

Requirements
Must have
• My project must have my logo.

A nice colour scheme comfortable to the eye.
Nice to have
• Nice eye catching design that will draw the end user to the page.
Should not have
• Must not have any information that create unjustified expectaions.
Must not contain laudatory statements such as best, better, breakthrough, champions, or other statement that may create unjustified expecation of services.

```html
<!DOCTYPE html>
<html lang="en">
<head>
<meta charset="utf-8">
<title>Larchmont Orthopaedics – Facebook Cover</title>
<link href="https://fonts.googleapis.com/css2?family=Michroma&display=swap" rel="stylesheet">
<style>
  :root {
    --teal: #5bb5b0;
    --slate: #56616b;
    --ink: #4a5560;
    --white: #ffffff;
    --stage: #e9ecee;
    --photo-light: #eef0ee;
    --photo-warm: #e3ddd2;
    --photo-blue: #b9cde6;
  }
  html, body {
    margin: 0;
    padding: 0;
    width: 1200px;
    height: 706px;
    overflow: hidden;
    background: var(--stage);
    font-family: "Michroma", "Questrial", sans-serif;
  }
  .cover {
    position: absolute;
    left: 0;
    top: 39px;
    width: 1200px;
    height: 628px;
    background: var(--white);
    overflow: hidden;
  }
  .cover-photo {
    position: absolute;
    left: 380px;
    top: 0;
    width: 820px;
    height: 628px;
    background:
      linear-gradient(180deg, var(--photo-light) 0%, var(--photo-warm) 55%, var(--photo-blue) 88%, var(--photo-blue) 100%);
  }
  .cover-fade {
    position: absolute;
    left: 380px;
    top: 0;
    width: 320px;
    height: 628px;
    background: linear-gradient(90deg, var(--white) 0%, rgba(255,255,255,0.85) 35%, rgba(255,255,255,0) 100%);
  }
  .brand {
    position: absolute;
    left: 48px;
    top: 66px;
    display: flex;
    align-items: center;
    gap: 16px;
  }
  .brand-mark {
    width: 58px;
    height: 58px;
    background: var(--teal);
  }
  .brand-name {
    color: var(--ink);
    font-size: 22px;
    line-height: 30px;
    letter-spacing: 1px;
    font-weight: 400;
  }
  .services {
    position: absolute;
    left: 0;
    top: 194px;
    width: 480px;
  }
  .service {
    position: relative;
    height: 57px;
    margin-bottom: 17px;
    width: 476px;
    clip-path: polygon(0 0, 462px 0, 476px 50%, 462px 100%, 0 100%);
    color: var(--white);
    font-size: 15px;
    line-height: 57px;
    padding-left: 38px;
    box-sizing: border-box;
    letter-spacing: 0.3px;
  }
  .service--teal { background: var(--teal); }
  .service--slate { background: var(--slate); }
  .service-track {
    position: absolute;
    left: 432px;
    top: 28px;
    width: 1px;
    height: 222px;
    background: rgba(255,255,255,0.8);
  }
  .service-dot {
    position: absolute;
    left: 427px;
    width: 12px;
    height: 12px;
    border-radius: 50%;
    background: var(--white);
  }
  .footer {
    position: absolute;
    left: 0;
    top: 556px;
    width: 700px;
    height: 72px;
  }
  .contact {
    position: absolute;
    top: 585px;
    display: flex;
    align-items: center;
    gap: 6px;
    color: #2f3a44;
    font-size: 13px;
  }
  .contact--phone { left: 88px; }
  .contact--email { left: 275px; }
  .contact-icon { width: 32px; height: 32px; }
</style>
</head>
<body>
  <div class="cover">
    <div class="cover-photo" role="img" aria-label="Photograph of a doctor examining a patient's raised leg on a treatment mat in a bright clinic room with shelves"></div>
    <div class="cover-fade"></div>

    <div class="brand">
      <div class="brand-mark"></div>
      <div class="brand-name">LARCHMONT<br>ORTHOPAEDICS</div>
    </div>

    <div class="services">
      <div class="service service--teal">TOTAL KNEE REPLACEMENTS</div>
      <div class="service service--slate">TOTAL HIP REPLACEMENTS</div>
      <div class="service service--teal">SPORTS INJURY OF THE KNEE</div>
      <div class="service service--slate">HIP FRACTURES</div>
      <div class="service-track"></div>
      <div class="service-dot" style="top:22px"></div>
      <div class="service-dot" style="top:96px"></div>
      <div class="service-dot" style="top:170px"></div>
      <div class="service-dot" style="top:244px"></div>
    </div>

    <svg class="footer" viewBox="0 0 700 72" aria-hidden="true">
      <polygon points="0,6 685,12 697,72 0,72" fill="#ffffff"/>
      <polyline points="0,6 685,12 697,72" fill="none" stroke="var(--teal)" stroke-width="3"/>
    </svg>

    <div class="contact contact--phone">
      <svg class="contact-icon" viewBox="0 0 32 32" aria-hidden="true">
        <circle cx="16" cy="16" r="16" fill="var(--teal)"/>
        <path d="M11 9.5c.6-.4 1.3-.3 1.7.3l1.6 2.4c.3.5.2 1.1-.2 1.5l-1 .9c.8 1.7 2.1 3 3.8 3.8l.9-1c.4-.4 1-.5 1.5-.2l2.4 1.6c.6.4.7 1.1.3 1.7l-.9 1.2c-.5.7-1.4 1-2.2.7-4-1.4-7.1-4.5-8.5-8.5-.3-.8 0-1.7.7-2.2z" fill="#ffffff"/>
      </svg>
      <span>55-555-0142</span>
    </div>
    <div class="contact contact--email">
      <svg class="contact-icon" viewBox="0 0 32 32" aria-hidden="true">
        <circle cx="16" cy="16" r="16" fill="var(--slate)"/>
        <rect x="9" y="11" width="14" height="10" fill="none" stroke="#ffffff" stroke-width="1.5"/>
        <polyline points="9,11 16,17 23,11" fill="none" stroke="#ffffff" stroke-width="1.5"/>
      </svg>
      <span>INFO@LARCHMONTORTHO.COM</span>
    </div>
  </div>
</body>
</html>
```